Mediation service showing compassion, collaboration, and resolution

I would like to purchase a customized version of a design you have previously submitted - https://www.brieflyart.example/design/48172036

Hello,

I would like a design for a flyer for my mediation business.
I also want to include a message that says that I offer rates on sliding scale.
My website is: www.morvenpeaceadr.example

Let me know what other details you might want?

Thank you,

Tobias

Target Market(s)

Local community, western Massachusetts USA. Businesses, families, individuals.

Industry/Entity Type

Mediation, Legal, Alternative Dispute Resolution, Divorce, Unions

Font styles to use
Sans Serif

Colors
0094D4
00A9DD
6FCCEA
C7EBF8
E9F6FB
00AB8E
00BBA5
67D7C9
C6EFE9
E9F9F6

Requirements
Must have
• “Sliding scale rates available “. Phone and email details. +1.555.784.3091 and email: tobias@morvenpeaceadr.example as well as we code to my website www.morvenpeaceadr.example

```html
<!DOCTYPE html>
<html lang="en">
<head>
<meta charset="utf-8">
<title>Sliding Scale Mediation Flyer</title>
<link rel="stylesheet" href="https://fonts.googleapis.com/css2?family=Arvo:wght@400;700&family=Oswald:wght@600&family=Kaushan+Script&display=swap">
<style>
  :root {
    --plum-light: #7a3670;
    --plum-dark: #5c2353;
    --plum-text: #5a2352;
    --navy: #424b7c;
    --cream: #f7e3bf;
    --ink: #2c2c2c;
    --footer: #2f2f2f;
    --white: #ffffff;
    --muted: #7a7a7a;
    --brand-blue: #0094D4;
    --brand-sky: #6FCCEA;
    --brand-teal: #00AB8E;
    --brand-mint: #67D7C9;
    --brand-ice: #E9F6FB;
    --brand-foam: #E9F9F6;
  }
  * { box-sizing: border-box; margin: 0; padding: 0; }
  html, body { width: 800px; height: 1200px; overflow: hidden; background: #fff; }
  .flyer {
    position: relative; width: 800px; height: 1200px; overflow: hidden;
    background: var(--white); font-family: "Arvo", serif; color: var(--ink);
  }
  .shapes { position: absolute; inset: 0; }

  .brand { position: absolute; left: 40px; top: 50px; width: 280px; text-align: center; }
  .brand-name { font-family: "Arvo", serif; font-weight: 400; font-size: 28px; color: #333; letter-spacing: 0.5px; }
  .brand-tag { font-size: 9px; color: var(--muted); margin-top: 4px; letter-spacing: 0.3px; }

  .headline { position: absolute; left: 40px; top: 176px; width: 300px; }
  .headline-main {
    font-family: "Oswald", sans-serif; font-weight: 600; font-size: 60px;
    line-height: 1.05; color: var(--plum-text); letter-spacing: -0.5px; white-space: nowrap;
  }
  .headline-script {
    font-family: "Kaushan Script", cursive; font-size: 44px; color: #1e1e1e;
    line-height: 1; margin-top: -2px; letter-spacing: 1px; white-space: nowrap;
  }

  .confidential { position: absolute; left: 40px; top: 340px; width: 266px; }
  .confidential h2 { font-size: 17px; font-weight: 700; color: var(--plum-text); margin-bottom: 14px; }
  .confidential p { font-size: 10.5px; line-height: 1.4; color: #222; }
  .source-link {
    display: inline-block; margin-top: 20px; background: var(--plum-light); color: var(--white);
    font-size: 10px; padding: 6px 10px; border-radius: 14px; width: 268px; white-space: nowrap;
  }

  .blob-text { position: absolute; color: var(--white); }
  .blob-text h2 { font-size: 18px; font-weight: 700; margin-bottom: 8px; letter-spacing: 0.3px; }
  .blob-text p { font-size: 10.5px; line-height: 1.38; }
  .what { left: 384px; top: 50px; width: 352px; }
  .why { left: 384px; top: 266px; width: 360px; }
  .why p { margin-bottom: 6px; }
  .services { left: 94px; top: 650px; width: 300px; }
  .services h2 { margin-bottom: 12px; }

  .ticks { list-style: none; }
  .ticks li { position: relative; padding-left: 20px; font-size: 10.5px; line-height: 1.3; }
  .why .ticks li { margin-bottom: 15px; }
  .services .ticks li { margin-bottom: 15.5px; }
  .ticks li::before {
    content: ""; position: absolute; left: 0; top: 2px; width: 8px; height: 8px;
    border: 1px solid var(--white); border-radius: 1px;
  }
  .ticks li::after {
    content: ""; position: absolute; left: 3px; top: 1px; width: 3px; height: 6px;
    border: solid var(--white); border-width: 0 1.5px 1.5px 0; transform: rotate(40deg);
  }

  .handshake-art {
    position: absolute; left: 440px; top: 560px; width: 326px; height: 470px;
    border-radius: 40px 40px 10px 10px;
    background: linear-gradient(160deg, #8d8fc4 0%, #5e4a9e 45%, #3a2b6e 100%);
    opacity: 0.9;
  }

  .badges { position: absolute; left: 430px; top: 1050px; display: flex; gap: 22px; align-items: center; }
  .badge { width: 94px; height: 34px; background: var(--brand-ice); border-radius: 4px; }
  .badge.round { width: 82px; background: var(--brand-foam); border-radius: 17px; }
  .badge.wide { width: 142px; background: #efe8d6; }

  .footer {
    position: absolute; left: 0; bottom: 0; width: 800px; height: 76px; background: var(--footer);
    display: flex; flex-direction: column; align-items: center; justify-content: center; gap: 6px;
    color: var(--white);
  }
  .footer-row { display: flex; align-items: center; justify-content: center; gap: 20px; }
  .footer-row.main { font-size: 16px; }
  .footer-row.contact { font-size: 12px; color: var(--brand-foam); }
  .footer-item { display: flex; align-items: center; gap: 8px; white-space: nowrap; }
  .footer-divider { width: 1px; height: 16px; background: #888; }
</style>
</head>
<body>
<div class="flyer">
  <svg class="shapes" width="800" height="1200" viewBox="0 0 800 1200" aria-hidden="true">
    <path d="M430 600 C520 560 640 580 720 610 C790 640 790 700 720 720 C640 740 560 700 470 690 C400 680 360 640 430 600 Z" fill="var(--cream)"/>
    <path d="M362 60 C392 25 520 32 620 30 C720 28 780 40 778 110 C776 180 760 200 770 240 L358 240 C352 180 348 100 362 60 Z" fill="var(--plum-light)"/>
    <path d="M358 240 L770 240 C790 330 760 420 776 500 C786 560 720 580 600 578 C480 576 380 580 352 530 C330 470 372 420 362 360 C356 300 350 270 358 240 Z" fill="var(--plum-dark)"/>
    <path d="M70 640 C110 600 260 610 360 632 C420 650 410 720 390 770 C370 830 400 900 400 970 C402 1050 340 1110 220 1108 C110 1106 50 1070 44 1010 C38 940 70 900 62 830 C54 760 30 690 70 640 Z" fill="var(--navy)"/>
  </svg>

  <div class="brand">
    <div class="brand-name">Tobias F Morven</div>
    <div class="brand-tag">Alternative Dispute Resolution</div>
  </div>

  <div class="headline">
    <div class="headline-main">OFFER RATES</div>
    <div class="headline-script">on sliding scale</div>
  </div>

  <section class="confidential">
    <h2>Is it confidential?</h2>
    <p>All communications in mediation are confidential, and neither the mediator's work product nor the participants' statements made in mediation about the subject matter can be disclosed later or admitted into evidence if a trial is held. Private sessions between a single party and the mediator have a second level of confidentiality, since they aren't shared with the other party without permission. The only record of a mediation is the written agreement reached by the parties.</p>
    <span class="source-link">https://www.stateinfo.example/about-mediation</span>
  </section>

  <section class="blob-text what">
    <h2>What is Mediation?</h2>
    <p>Mediation is a form of facilitated negotiation, by a mediator, who helps the parties engage in a dialog to search for a joint agreement. All decisions, from agreeing to participate in the mediation, to possible terms of an agreement, are decided by the parties. The mediator has no authority over the parties nor impose any directives. The mediator is there to help the parties find their interests, list and organize the options they have vs the alternatives and the outcome probabilities for each outside a resolution via the mediation process.</p>
  </section>

  <section class="blob-text why">
    <h2>Why Mediation?</h2>
    <p>There are many advantages to mediation, and below is a list of a few</p>
    <ul class="ticks">
      <li>Saves parties time and money</li>
      <li>Allows parties to resolve disputes in accordance with own preferences</li>
      <li>Confidential, private forum for addressing sensitive issues and exploring settlment</li>
      <li>Parties control selection of mediator</li>
      <li>Parties retain control over outcome; can end mediation at any time</li>
      <li>Allows for creativity and flexibility in generating options; leads to solutions tailored to meet parties' interests</li>
    </ul>
  </section>

  <div class="handshake-art" role="img" aria-label="Illustration of two businessmen shaking hands"></div>

  <section class="blob-text services">
    <h2>Services Provided</h2>
    <ul class="ticks">
      <li>Divorce and Family Mediation (Sliding scale rates)</li>
      <li>Commercial and business related Mediation</li>
      <li>International business and trading conflict mediation</li>
      <li>Merger Negotiations &amp; Business Collaboration</li>
      <li>Mediation between dealer, agent, distributor and supplier, manufacturer</li>
      <li>Contract negotiation consultancy</li>
      <li>Employment contract negotiations</li>
      <li>Mediation for property or entity division</li>
      <li>Workplace Mediation</li>
      <li>Mediation Coaching</li>
      <li>Ombuds contracting</li>
      <li>Mediation via videoconference</li>
      <li>Meetings Facilitation</li>
    </ul>
  </section>

  <div class="badges" aria-label="Membership badges">
    <div class="badge"></div>
    <div class="badge round"></div>
    <div class="badge wide"></div>
  </div>

  <footer class="footer">
    <div class="footer-row main">
      <div class="footer-item">
        <svg width="13" height="17" viewBox="0 0 14 18" aria-hidden="true"><path d="M7 1 C3.5 1 1 3.6 1 7 C1 11 7 17 7 17 C7 17 13 11 13 7 C13 3.6 10.5 1 7 1 Z" fill="none" stroke="#f0c66a" stroke-width="2"/><circle cx="7" cy="7" r="2" fill="#f0c66a"/></svg>
        <span>88 Linden Row #12, Fairhollow MA 01999 USA</span>
      </div>
      <div class="footer-divider"></div>
      <div class="footer-item">
        <svg width="14" height="14" viewBox="0 0 14 14" aria-hidden="true"><circle cx="7" cy="7" r="6" fill="none" stroke="var(--brand-sky)" stroke-width="1.3"/><ellipse cx="7" cy="7" rx="2.6" ry="6" fill="none" stroke="var(--brand-sky)" stroke-width="1.1"/><line x1="1" y1="7" x2="13" y2="7" stroke="var(--brand-sky)" stroke-width="1.1"/></svg>
        <span>www.morvenpeaceadr.example</span>
      </div>
    </div>
    <div class="footer-row contact">
      <div class="footer-item">
        <svg width="12" height="12" viewBox="0 0 12 12" aria-hidden="true"><path d="M2.5 1 L4.5 1 L5.5 3.8 L4.2 4.8 C4.8 6 6 7.2 7.2 7.8 L8.2 6.5 L11 7.5 L11 9.5 C11 10.3 10.3 11 9.5 11 C5 11 1 7 1 2.5 C1 1.7 1.7 1 2.5 1 Z" fill="var(--brand-mint)"/></svg>
        <span>+1.555.784.3091</span>
      </div>
      <div class="footer-divider"></div>
      <div class="footer-item">
        <svg width="14" height="11" viewBox="0 0 14 11" aria-hidden="true"><rect x="0.7" y="0.7" width="12.6" height="9.6" rx="1" fill="none" stroke="var(--brand-mint)" stroke-width="1.3"/><path d="M1 1.2 L7 6 L13 1.2" fill="none" stroke="var(--brand-mint)" stroke-width="1.3"/></svg>
        <span>tobias@morvenpeaceadr.example</span>
      </div>
    </div>
  </footer>
</div>
</body>
</html>
```